Care recruitment flyers

We are starting a new care recruitment business and would like to design two flyers:

1. For people wanting to work in care;
2. For customers wanting to hire care staff.

Files are uploaded with copy. Please do not use the typeface and colour used as a guide.

Flyer 1 should have a professional yet informal style about it and promote the benefits of being an excellent carer with the opportunities to progress and earn more money.

Flyer 2 should be more professional, structured approach with perhaps a newspaper article style. The essence being we are providing the answer to a common problem in the care sector of finding reliable care staff.

Copy is provided for both flyers but can be re-arranged or tweeked to suit the design.

Target Market(s)

Flyer 1 to attract care staff - predominantly a female market. We are looking to recruit care staff to work for care homes.

Flyer 2 to attract hirers - this will be care home managers who are also predominantly female. We are looking to offer talented and reliable care staff to care homes on a temporary basis.

Industry/Entity Type

Business

Font styles to use
Sans Serif

Requirements
Must have
• Designs must include the logo and star imagery provided. Both flyers must be two sided A4 size in full colour.
Nice to have
• Would like the designs to include imagery of care staff (care assistant in uniform).
Should not have
• No elderly people.

```html
<!DOCTYPE html>
<html lang="en">
<head>
<meta charset="utf-8">
<title>Kindhand – Care Recruitment Flyer</title>
<link rel="stylesheet" href="https://fonts.googleapis.com/css2?family=Questrial&family=Arimo:wght@400;700&display=swap">
<style>
  :root {
    --stage: #000000;
    --red-bright: #d52b3a;
    --red-deep: #8f1b3b;
    --wine: #a51d36;
    --gold: #f7c31c;
    --orange: #f7a21b;
    --orange-deep: #f07a1d;
    --ink: #333333;
    --paper: #ffffff;
  }
  * { box-sizing: border-box; margin: 0; padding: 0; }
  html, body { width: 1200px; height: 1000px; overflow: hidden; background: var(--stage); }
  .canvas { position: relative; width: 1200px; height: 1000px; background: var(--stage); }

  .page { position: absolute; top: 99px; width: 552px; height: 780px; overflow: hidden; }
  .page--front { left: 41px; background: linear-gradient(100deg, var(--red-bright), var(--red-deep)); }
  .page--back { left: 613px; background: var(--paper); }

  .page-label {
    position: absolute; top: 908px; width: 300px; text-align: center;
    font-family: "Questrial", sans-serif; font-size: 38px; color: var(--paper);
  }
  .page-label--front { left: 216px; }
  .page-label--back { left: 739px; }

  .deco { position: absolute; display: block; }

  /* Front */
  .front-photo { position: absolute; inset: 0; }
  .front-headline {
    position: absolute; top: 28px; left: 0; width: 100%; text-align: center;
    font-family: "Questrial", sans-serif; font-weight: 400; color: var(--paper); line-height: 1.17;
  }
  .front-headline__lead { font-size: 34.5px; display: block; }
  .front-headline__accent { font-size: 41px; color: var(--gold); display: block; }
  .front-headline__close { font-size: 41px; display: block; }
  .brand-badge {
    position: absolute; left: 329px; top: 172px; width: 194px; height: 194px;
    border-radius: 50%; background: var(--paper); border: 4px solid var(--wine);
    display: flex; align-items: center; justify-content: center;
  }
  .brand-badge__name { font-family: "Questrial", sans-serif; font-size: 36px; color: var(--orange-deep); }

  /* Back */
  .back-title { position: absolute; left: 34px; top: 32px; font-family: "Arimo", sans-serif; }
  .back-title__kicker { display: block; font-family: "Questrial", sans-serif; font-weight: 400; font-size: 35px; color: var(--orange); line-height: 1.05; }
  .back-title__main { display: block; font-size: 36px; font-weight: 700; color: var(--wine); line-height: 1.1; letter-spacing: -0.5px; }
  .back-intro {
    position: absolute; left: 34px; top: 111px; width: 472px;
    font-family: "Arimo", sans-serif; font-size: 12.6px; line-height: 1.38; color: #555;
  }
  .back-pill {
    position: absolute; left: 34px; top: 188px; height: 33px; padding: 0 12px;
    background: var(--wine); border-radius: 9px; color: var(--paper);
    font-family: "Arimo", sans-serif; font-size: 20.5px; line-height: 33px; letter-spacing: 0.3px;
  }
  .benefits { position: absolute; left: 34px; top: 233px; width: 476px; list-style: none;
    font-family: "Arimo", sans-serif; font-size: 17px; line-height: 23px; color: var(--ink); }
  .benefits__item { position: relative; padding-left: 31px; margin-bottom: 8px; }
  .benefits__item--short { margin-bottom: 11px; }
  .benefits__icon { position: absolute; left: 0; top: 4px; width: 18px; height: 16px; }
  .benefits strong { font-weight: 700; }
  .back-footer-band { position: absolute; inset: 0; }
  .cta-text {
    position: absolute; left: 34px; top: 654px; font-family: "Arimo", sans-serif;
    font-size: 20px; line-height: 27px; color: var(--paper);
  }
  .cta-divider { position: absolute; left: 295px; top: 680px; width: 1px; height: 50px; background: var(--paper); }
  .cta-contact { position: absolute; left: 317px; top: 678px; font-family: "Arimo", sans-serif; }
  .cta-contact__phone { display: block; font-size: 29.5px; font-weight: 700; color: var(--orange); letter-spacing: -0.3px; }
  .cta-contact__web { display: block; margin-top: 1px; font-size: 18.5px; font-weight: 700; color: var(--paper); }
</style>
</head>
<body>
<div class="canvas">

  <section class="page page--front">
    <svg class="front-photo" width="552" height="780" viewBox="0 0 552 780">
      <defs>
        <linearGradient id="photoTone" x1="0" y1="0" x2="1" y2="1">
          <stop offset="0" stop-color="#4a66b8"/>
          <stop offset="0.45" stop-color="#5f7cc6"/>
          <stop offset="0.62" stop-color="#d9b7a2"/>
          <stop offset="0.78" stop-color="#e8c9b6"/>
          <stop offset="0.9" stop-color="#f2f3f6"/>
          <stop offset="1" stop-color="#5a76c2"/>
        </linearGradient>
        <linearGradient id="arcTone" x1="0" y1="0" x2="1" y2="0">
          <stop offset="0" stop-color="#f7a21b"/>
          <stop offset="1" stop-color="#f07a1d"/>
        </linearGradient>
      </defs>
      <path role="img" aria-label="Photo of a care assistant in blue scrubs with a stethoscope, writing notes on a clipboard"
            d="M0,460 C90,300 330,225 552,232 L552,780 L0,780 Z" fill="url(#photoTone)"/>
      <path d="M0,460 C90,300 330,225 552,232" fill="none" stroke="url(#arcTone)" stroke-width="9"/>
    </svg>
    <h1 class="front-headline">
      <span class="front-headline__lead">Do you want to be rewarded for</span>
      <span class="front-headline__accent">being an Excellent Carer?</span>
      <span class="front-headline__close">Look no further</span>
    </h1>
    <svg class="deco" style="left:49px;top:128px;width:68px;height:68px;transform:rotate(-15deg)" viewBox="0 0 100 100"><path d="M50 90 C20 70 5 50 5 32 C5 15 18 5 32 5 C41 5 47 10 50 17 C53 10 59 5 68 5 C82 5 95 15 95 32 C95 50 80 70 50 90Z" fill="#f48a2a"/></svg>
    <svg class="deco" style="left:134px;top:196px;width:34px;height:34px;transform:rotate(-10deg)" viewBox="0 0 100 100"><polygon points="50,3 62,38 98,38 69,60 80,95 50,74 20,95 31,60 2,38 38,38" fill="#e2262f"/></svg>
    <svg class="deco" style="left:498px;top:140px;width:25px;height:25px" viewBox="0 0 100 100"><polygon points="50,3 62,38 98,38 69,60 80,95 50,74 20,95 31,60 2,38 38,38" fill="#f49a27"/></svg>
    <div class="brand-badge"><span class="brand-badge__name">kindhand</span></div>
  </section>

  <section class="page page--back">
    <svg class="back-footer-band" width="552" height="780" viewBox="0 0 552 780">
      <defs>
        <linearGradient id="bandTone" x1="0" y1="0" x2="1" y2="0">
          <stop offset="0" stop-color="#8f1b3b"/>
          <stop offset="1" stop-color="#d52b3a"/>
        </linearGradient>
      </defs>
      <path d="M0,545 C140,640 470,610 552,380 L552,780 L0,780 Z" fill="url(#bandTone)"/>
      <path d="M0,545 C140,640 470,610 552,380" fill="none" stroke="var(--orange)" stroke-width="8"/>
    </svg>
    <svg class="deco" style="left:335px;top:459px;width:84px;height:84px;transform:rotate(12deg)" viewBox="0 0 100 100"><polygon points="50,3 62,38 98,38 69,60 80,95 50,74 20,95 31,60 2,38 38,38" fill="#b01e37"/></svg>
    <svg class="deco" style="left:419px;top:433px;width:44px;height:44px;transform:rotate(12deg)" viewBox="0 0 100 100"><path d="M50 90 C20 70 5 50 5 32 C5 15 18 5 32 5 C41 5 47 10 50 17 C53 10 59 5 68 5 C82 5 95 15 95 32 C95 50 80 70 50 90Z" fill="#c0203a"/></svg>
    <svg class="deco" style="left:405px;top:585px;width:66px;height:66px;transform:rotate(-8deg)" viewBox="0 0 100 100"><polygon points="50,3 62,38 98,38 69,60 80,95 50,74 20,95 31,60 2,38 38,38" fill="#f7a23a"/></svg>
    <svg class="deco" style="left:469px;top:563px;width:32px;height:32px;transform:rotate(-10deg)" viewBox="0 0 100 100"><path d="M50 90 C20 70 5 50 5 32 C5 15 18 5 32 5 C41 5 47 10 50 17 C53 10 59 5 68 5 C82 5 95 15 95 32 C95 50 80 70 50 90Z" fill="#f49a3a"/></svg>

    <h2 class="back-title">
      <span class="back-title__kicker">RECRUITING NOW FOR</span>
      <span class="back-title__main">CARE AND SUPPORT STAFF</span>
    </h2>
    <p class="back-intro">Kindhand are looking for talented, experienced and reliable care and support staff. We believe that care staff should be rewarded for the great work they do. We are a specialist care agency in the area with assignments arriving daily.</p>
    <div class="back-pill">Our clients are looking for you.</div>

    <ul class="benefits">
      <li class="benefits__item"><svg class="benefits__icon" viewBox="0 0 18 16"><path d="M9 15 L1.5 7.5 A4 4 0 0 1 9 3 A4 4 0 0 1 16.5 7.5 Z" fill="var(--orange)"/></svg>We offer a reward system that pays you a <strong>higher hourly rate</strong> based on your performance and we offer <strong>full training and development</strong> opportunities.</li>
      <li class="benefits__item"><svg class="benefits__icon" viewBox="0 0 18 16"><path d="M9 15 L1.5 7.5 A4 4 0 0 1 9 3 A4 4 0 0 1 16.5 7.5 Z" fill="var(--orange)"/></svg><strong>Not experienced?</strong> If you have the right personality and attitude and wish to become a talented carer, we can also help you.</li>
      <li class="benefits__item"><svg class="benefits__icon" viewBox="0 0 18 16"><path d="M9 15 L1.5 7.5 A4 4 0 0 1 9 3 A4 4 0 0 1 16.5 7.5 Z" fill="var(--orange)"/></svg><strong>Know other people who might be interested?</strong><br>Referral scheme in place.</li>
      <li class="benefits__item benefits__item--short"><svg class="benefits__icon" viewBox="0 0 18 16"><path d="M9 15 L1.5 7.5 A4 4 0 0 1 9 3 A4 4 0 0 1 16.5 7.5 Z" fill="var(--orange)"/></svg><strong>Great rates of pay</strong></li>
      <li class="benefits__item benefits__item--short"><svg class="benefits__icon" viewBox="0 0 18 16"><path d="M9 15 L1.5 7.5 A4 4 0 0 1 9 3 A4 4 0 0 1 16.5 7.5 Z" fill="var(--orange)"/></svg><strong>Training opportunities offered</strong></li>
      <li class="benefits__item"><svg class="benefits__icon" viewBox="0 0 18 16"><path d="M9 15 L1.5 7.5 A4 4 0 0 1 9 3 A4 4 0 0 1 16.5 7.5 Z" fill="var(--orange)"/></svg><strong>Uniform provided</strong></li>
    </ul>

    <p class="cta-text">Be part of a rewarding<br>agency and call us now<br>for an informal discussion:</p>
    <div class="cta-divider"></div>
    <div class="cta-contact">
      <span class="cta-contact__phone">0870 555 01 46</span>
      <span class="cta-contact__web">www.kindhand.agency</span>
    </div>
  </section>

  <div class="page-label page-label--front">Front Page</div>
  <div class="page-label page-label--back">Back Page</div>
</div>
</body>
</html>
```